Orva Business Card

we need a business card for flooring business called Orva Flooring, the design should be black and white. we have 2 locations

Calderwood Showroom
527 Kellerman Road,
Calderwood VIC 3167

Ashmere Showroom
462 Bramwell Hwy,
Ashmere VIC 3192

email : sales@orvaflooring.com.au
(03) 9471 2830

Please inform we sell , Laminate, Hybrid, Timber, carpet and commercial flooring

```html
<!DOCTYPE html>
<html lang="en">
<head>
<meta charset="utf-8">
<title>Orva Flooring Business Card</title>
<link rel="stylesheet" href="https://fonts.googleapis.com/css2?family=Montserrat:wght@400;500;700&display=swap">
<style>
  :root {
    --ink: #0d0d0d;
    --paper: #ffffff;
    --card-black: #141414;
    --backdrop: #d9d9d9;
    --soft-white: #e8e8e8;
    --muted: #bdbdbd;
  }
  * { box-sizing: border-box; margin: 0; padding: 0; }
  html, body {
    width: 1200px; height: 801px; overflow: hidden;
    background: var(--backdrop);
    font-family: "Montserrat", sans-serif;
  }
  .stage {
    width: 1200px; height: 801px;
    display: flex; align-items: center; justify-content: center; gap: 48px;
  }
  .card {
    width: 540px; height: 309px;
    position: relative; overflow: hidden;
    box-shadow: 0 6px 18px rgba(0,0,0,0.18);
  }
  /* front */
  .card-front { background: var(--paper); color: var(--ink); }
  .front-top {
    height: 190px; display: flex; align-items: center; padding: 0 32px;
  }
  .brand {
    width: 170px; text-align: center;
    font-weight: 400; color: #3a3a3a; letter-spacing: 3px; line-height: 1.25;
  }
  .brand .brand-main { display: block; font-size: 34px; }
  .brand .brand-sub { display: block; font-size: 16px; }
  .divider { width: 1px; height: 112px; background: var(--ink); margin: 0 24px 0 14px; }
  .person .name { font-weight: 700; font-size: 24px; letter-spacing: 1px; }
  .person .role { font-size: 11px; font-weight: 500; letter-spacing: 0.5px; margin: 2px 0 12px; }
  .contact { display: flex; align-items: center; gap: 8px; font-size: 13.5px; margin-top: 5px; }
  .contact svg { width: 13px; height: 13px; flex: none; }
  .front-band {
    position: absolute; left: 0; right: 0; bottom: 0; height: 119px;
    background: var(--ink); color: var(--paper);
    display: flex; justify-content: space-between; align-items: center;
    padding: 0 30px; font-size: 13px; line-height: 1.45;
  }
  .showroom-right { text-align: right; }
  /* back */
  .card-back {
    background: var(--card-black); color: var(--soft-white);
    display: flex; flex-direction: column; align-items: center; justify-content: center;
  }
  .card-back .brand { width: auto; color: var(--muted); }
  .card-back .brand-main { font-size: 56px; letter-spacing: 6px; }
  .card-back .brand-sub { font-size: 26px; letter-spacing: 5px; }
  .tagline {
    margin-top: 26px; text-align: center; font-size: 14px; line-height: 1.4; color: var(--soft-white);
  }
</style>
</head>
<body>
<main class="stage">
  <section class="card card-front">
    <div class="front-top">
      <div class="brand"><span class="brand-main">ORVA</span><span class="brand-sub">FLOORING</span></div>
      <div class="divider"></div>
      <div class="person">
        <p class="name">MARCUS HALE</p>
        <p class="role">MANAGING DIRECTOR</p>
        <p class="contact">
          <svg viewBox="0 0 24 24" aria-hidden="true"><path fill="#0d0d0d" d="M6.6 10.8a15 15 0 0 0 6.6 6.6l2.2-2.2a1 1 0 0 1 1-.25 11.4 11.4 0 0 0 3.6.57 1 1 0 0 1 1 1V20a1 1 0 0 1-1 1A17 17 0 0 1 3 4a1 1 0 0 1 1-1h3.5a1 1 0 0 1 1 1 11.4 11.4 0 0 0 .57 3.6 1 1 0 0 1-.25 1z"/></svg>
          (03) 9471 2830
        </p>
        <p class="contact">
          <svg viewBox="0 0 24 24" aria-hidden="true"><path fill="#0d0d0d" d="M2 5h20v14H2z"/><path fill="none" stroke="#fff" stroke-width="1.6" d="M2.5 5.5 12 13l9.5-7.5M2.5 18.5l7-6.5M21.5 18.5l-7-6.5"/></svg>
          sales@orvaflooring.com.au
        </p>
      </div>
    </div>
    <div class="front-band">
      <p class="showroom">Ashmere Showroom<br>462 Bramwell Hwy,<br>Ashmere VIC 3192</p>
      <p class="showroom showroom-right">Calderwood Showroom<br>527 Kellerman Road,<br>Calderwood VIC 3167</p>
    </div>
  </section>

  <section class="card card-back">
    <div class="brand"><span class="brand-main">ORVA</span><span class="brand-sub">FLOORING</span></div>
    <p class="tagline">we sell , Laminate, Hybrid, Timber,<br>carpet and commercial flooring</p>
  </section>
</main>
</body>
</html>
```